Roadward Lane Management Company Website

Modern website Wordpress design using all greyscale photos with a pop of red (such as road closure signs or detour cones) for strategic emphasis. (see brand guide for color codes)
The creative goal is to leverage high-contrast, desaturated imagery to create a clean, professional, and industrial feel. The selective use of red will draw immediate attention to critical elements—such as road hazards, safety equipment, or key messages to ensure the viewer's focus is directed with purpose.

Brand guide, homepage content and logo are attached. Create clean professional user experience to market services to industry professionals.

```html
<!DOCTYPE html>
<html lang="en">
<head>
<meta charset="utf-8">
<title>Roadward Lane Management Company</title>
<link href="https://fonts.googleapis.com/css2?family=Inter:wght@400;500;600;700&display=swap" rel="stylesheet">
<style>
:root{
  --red:#e31b23;
  --ink:#111111;
  --text:#555a60;
  --light:#f6f7f9;
  --pink:#fbeff0;
  --white:#ffffff;
  --black:#000000;
  --line:#e6e8eb;
}
*{box-sizing:border-box;margin:0;padding:0}
html,body{width:1200px;height:2240px;overflow:hidden}
body{font-family:"Inter",Arial,sans-serif;color:var(--ink);background:var(--white);position:relative}
.wrap{width:930px;margin:0 auto;position:relative}
svg{display:block}

/* nav */
.nav{height:50px;background:var(--white);box-shadow:0 1px 4px rgba(0,0,0,.06);position:relative;z-index:2}
.nav .wrap{display:flex;align-items:center;justify-content:space-between;height:50px}
.brand{display:flex;align-items:center;gap:7px;font-weight:700;font-size:17px;color:var(--ink)}
.brand-mark{width:14px;height:14px;background:var(--red)}
.menu{display:flex;align-items:center;gap:20px;font-size:11px;margin-right:-18px}
.menu .active{color:var(--red)}
.menu .cta{background:var(--red);color:var(--white);padding:7px 7px;border-radius:2px;font-size:12px;font-weight:500}

/* hero */
.hero{height:375px;position:relative;background:linear-gradient(90deg,#1e1e1e 0%,#3a3a3a 45%,#555 70%,#2c2c2c 100%);overflow:hidden}
.hero-photo{position:absolute;inset:0;background:linear-gradient(180deg,rgba(0,0,0,.15),rgba(0,0,0,.35))}
.hero .wrap{padding-top:104px;position:relative}
.hero h1{color:var(--white);font-size:30px;line-height:30px;font-weight:700;letter-spacing:-.3px}
.hero p{color:#eee;font-size:12px;line-height:17px;margin-top:20px;width:430px}
.btn{display:inline-block;background:var(--red);color:var(--white);font-weight:600;border-radius:3px}
.hero .btn{margin-top:22px;font-size:11px;padding:12px 20px}

/* band */
.band{height:130px;background:var(--black);text-align:center;color:var(--white);padding-top:41px}
.band h2{font-size:18px;font-weight:700;letter-spacing:-.2px}
.band p{font-size:12px;color:#ddd;margin-top:12px}

/* services */
.services{height:451px;background:var(--light);padding-top:51px}
.sec-title{text-align:center;font-size:18px;font-weight:700}
.sec-sub{text-align:center;font-size:12px;color:var(--text);margin-top:12px}
.grid4{display:grid;grid-template-columns:repeat(4,221px);gap:15px;margin-top:36px}
.svc{background:var(--white);border-radius:4px;box-shadow:0 2px 8px rgba(0,0,0,.07);height:142px;padding:23px 15px 0}
.svc svg{width:22px;height:22px;stroke:var(--red);fill:none;stroke-width:1.8}
.svc h3{font-size:12px;font-weight:600;margin-top:22px;letter-spacing:-.2px;white-space:nowrap}
.svc p{font-size:9.5px;line-height:15px;color:var(--text);margin-top:11px}

/* industries */
.industries{height:489px;background:var(--white);padding-top:50px}
.ind-body{display:flex;justify-content:space-between;margin-top:40px}
.ind-list{width:445px;display:flex;flex-direction:column;gap:20px}
.ind-item{height:60px;background:var(--light);border-radius:8px;display:flex;align-items:center;padding-left:15px;gap:11px;font-size:12px;font-weight:600}
.ind-icon{width:30px;height:30px;border-radius:50%;background:var(--pink);display:flex;align-items:center;justify-content:center}
.ind-icon svg{width:14px;height:14px;stroke:var(--red);fill:none;stroke-width:1.8}
.ind-photo{width:445px;height:296px;border-radius:8px;background:linear-gradient(135deg,#8b8b8b,#5d5d5d 55%,#a5a5a5);position:relative;box-shadow:0 6px 18px rgba(0,0,0,.12)}
.badge{position:absolute;right:-15px;bottom:-15px;width:60px;height:60px;border-radius:50%;background:var(--red);color:var(--white);text-align:center;padding-top:15px}
.badge b{display:block;font-size:14px}
.badge span{font-size:8px}

/* why */
.why{height:496px;background:var(--light);padding-top:55px}
.grid-why{display:grid;grid-template-columns:repeat(4,217px);gap:21px;margin-top:40px}
.why-card{background:var(--white);border-radius:8px;box-shadow:0 2px 10px rgba(0,0,0,.07);height:181px;padding:20px 20px 0}
.why-icon{width:40px;height:40px;border-radius:50%;background:var(--pink);display:flex;align-items:center;justify-content:center}
.why-icon svg{width:17px;height:17px;stroke:var(--red);fill:none;stroke-width:1.8}
.why-card h3{font-size:12px;font-weight:600;margin-top:17px;letter-spacing:-.2px;white-space:nowrap}
.why-card p{font-size:9.5px;line-height:15px;color:var(--text);margin-top:11px}
.more{display:flex;align-items:center;gap:6px;color:var(--red);font-size:8.5px;font-weight:600;margin-top:13px}
.stats{margin-top:41px;height:85px;background:var(--pink);border-radius:10px;display:flex;align-items:center;padding:0 20px;justify-content:space-between}
.stat-row{display:flex;align-items:center}
.stat{text-align:center;padding:0 20px}
.stat:first-child{padding-left:0}
.stat+.stat{border-left:1px solid #dccbcd}
.stat b{display:block;color:var(--red);font-size:21px;font-weight:600}
.stat span{font-size:9.5px;color:var(--text)}
.stats .btn{font-size:11px;padding:12px 20px}

/* footer */
.footer{height:250px;background:var(--black);color:var(--white);padding-top:36px}
.fcols{display:flex}
.fcol{width:320px}
.fcol h4{font-size:12px;font-weight:600;margin-bottom:17px}
.fcol li{list-style:none;font-size:9.5px;margin-bottom:11px;display:flex;align-items:center;gap:9px}
.fcol li svg{width:10px;height:10px;stroke:var(--white);fill:none;stroke-width:2}
.socials{display:flex;gap:10px}
.socials span{width:25px;height:25px;border:1px solid #bbb;border-radius:50%}
.copy{border-top:1px solid #333;margin-top:26px;padding-top:22px;text-align:center;font-size:9.5px}
</style>
</head>
<body>
<header class="nav">
  <div class="wrap">
    <div class="brand"><span class="brand-mark"></span>Roadward</div>
    <nav class="menu">
      <span class="active">Home</span><span>About</span><span>Services</span><span>Rentals</span><span>Jobs</span><span class="cta">Contact</span>
    </nav>
  </div>
</header>

<section class="hero">
  <div class="hero-photo" role="img" aria-label="Greyscale photo of two road workers in hard hats walking toward a highway work zone with a crash attenuator truck and a red traffic cone"></div>
  <div class="wrap">
    <h1>Traffic Control Solutions<br>Engineered for Safety</h1>
    <p>Dedicated to safety, compliance, and efficient traffic flow. Your trusted partner in professional traffic management.</p>
    <span class="btn">Get a Quote</span>
  </div>
</section>

<section class="band">
  <h2>SAFETY ISN'T A PRIORITY, IT'S THE FOUNDATION OF EVERYTHING WE DO.</h2>
  <p>Ensuring compliance with TxDOT &amp; OSHA regulations</p>
</section>

<section class="services">
  <div class="wrap">
    <h2 class="sec-title">Our Services</h2>
    <div class="grid4">
      <div class="svc"><svg viewBox="0 0 24 24"><path d="M5 21V4h12l-2 4 2 4H5"/></svg><h3>Flagging &amp; Lane Closures</h3><p>Professional certified flaggers ensuring safe and efficient traffic flow.</p></div>
      <div class="svc"><svg viewBox="0 0 24 24"><path d="M12 21s-6-6-6-11a6 6 0 0 1 12 0c0 5-6 11-6 11z"/><circle cx="12" cy="10" r="2"/></svg><h3>Temporary Traffic Control Plans</h3><p>Custom TTCPs designed for maximum safety and minimal disruption.</p></div>
      <div class="svc"><svg viewBox="0 0 24 24"><rect x="8" y="3" width="8" height="18" rx="2"/><circle cx="12" cy="8" r="1.3"/><circle cx="12" cy="12" r="1.3"/><circle cx="12" cy="16" r="1.3"/></svg><h3>Signage &amp; Barricades</h3><p>Complete range of high-visibility traffic control equipment.</p></div>
      <div class="svc"><svg viewBox="0 0 24 24"><path d="M12 3l7 3v6c0 5-3 8-7 9-4-1-7-4-7-9V6z"/><path d="M13 8l-3 5h4l-3 4"/></svg><h3>Crash Attenuators</h3><p>TMAs and impact protection for enhanced work zone safety.</p></div>
      <div class="svc"><svg viewBox="0 0 24 24"><rect x="2" y="7" width="12" height="9"/><path d="M14 10h4l3 3v3h-7"/><circle cx="6" cy="17" r="2"/><circle cx="17" cy="17" r="2"/></svg><h3>Heavy Highway Control</h3><p>Specialized solutions for major highway construction projects.</p></div>
      <div class="svc"><svg viewBox="0 0 24 24"><circle cx="6" cy="19" r="2"/><circle cx="18" cy="5" r="2"/><path d="M6 17V8a3 3 0 0 1 6 0v8a3 3 0 0 0 6 0V7"/></svg><h3>Roadway Detours</h3><p>Expert planning and implementation of traffic diversions.</p></div>
      <div class="svc"><svg viewBox="0 0 24 24"><path d="M6 3h9l4 4v14H6z"/><path d="M9 10h7M9 14h7M9 18h4"/></svg><h3>Safety Consulting</h3><p>TxDOT and OSHA compliance guidance and consulting.</p></div>
      <div class="svc"><svg viewBox="0 0 24 24"><circle cx="9" cy="8" r="4"/><path d="M2 21c0-4 3-7 7-7s7 3 7 7"/><path d="M16 4a4 4 0 0 1 0 8M18 14c3 1 4 4 4 7"/></svg><h3>Event Control</h3><p>Professional traffic and crowd management for events.</p></div>
    </div>
  </div>
</section>

<section class="industries">
  <div class="wrap">
    <h2 class="sec-title">Industries We Serve</h2>
    <p class="sec-sub">Our expertise spans across multiple sectors, providing specialized traffic control solutions for various industry needs.</p>
    <div class="ind-body">
      <div class="ind-list">
        <div class="ind-item"><span class="ind-icon"><svg viewBox="0 0 24 24"><path d="M12 21s-6-6-6-11a6 6 0 0 1 12 0c0 5-6 11-6 11z"/></svg></span>Road Construction &amp; Detours</div>
        <div class="ind-item"><span class="ind-icon"><svg viewBox="0 0 24 24"><path d="M3 9h18M4 21h16M6 9v12M10 9v12M14 9v12M18 9v12M3 9l9-5 9 5"/></svg></span>Municipal &amp; State Projects</div>
        <div class="ind-item"><span class="ind-icon"><svg viewBox="0 0 24 24"><path d="M4 21V9h6v12M10 21V4h8v17M2 21h20"/></svg></span>Private Sector &amp; Contractors</div>
        <div class="ind-item"><span class="ind-icon"><svg viewBox="0 0 24 24"><path d="M6 21V9l5-5h5v17zM10 13h4"/></svg></span>Oil, Gas, Wind, Solar &amp; Manufacturing</div>
      </div>
      <div class="ind-photo" role="img" aria-label="Greyscale photo of two site supervisors in hard hats and safety vests reviewing plans beside a road under an overpass">
        <div class="badge"><b>15+</b><span>Years Exp.</span></div>
      </div>
    </div>
  </div>
</section>

<section class="why">
  <div class="wrap">
    <h2 class="sec-title">Why Choose Us?</h2>
    <p class="sec-sub">We're committed to delivering excellence in every aspect of traffic control</p>
    <div class="grid-why">
      <div class="why-card"><span class="why-icon"><svg viewBox="0 0 24 24"><path d="M12 3l7 3v6c0 5-3 8-7 9-4-1-7-4-7-9V6z"/><path d="M9 12l2 2 4-4"/></svg></span><h3>TxDOT-Compliant &amp; Certified</h3><p>Meeting and exceeding all state and federal safety regulations.</p><span class="more">Learn More <svg width="8" height="8" viewBox="0 0 10 10"><path d="M1 5h7M5 2l3 3-3 3" stroke="currentColor" fill="none" stroke-width="1.3"/></svg></span></div>
      <div class="why-card"><span class="why-icon"><svg viewBox="0 0 24 24"><circle cx="12" cy="6" r="2.5"/><circle cx="5" cy="9" r="2"/><circle cx="19" cy="9" r="2"/><path d="M8 21v-6a4 4 0 0 1 8 0v6M2 19v-3a3 3 0 0 1 4-3M22 19v-3a3 3 0 0 0-4-3"/></svg></span><h3>Expert Team</h3><p>Professional crew with extensive industry experience.</p><span class="more">Learn More <svg width="8" height="8" viewBox="0 0 10 10"><path d="M1 5h7M5 2l3 3-3 3" stroke="currentColor" fill="none" stroke-width="1.3"/></svg></span></div>
      <div class="why-card"><span class="why-icon"><svg viewBox="0 0 24 24"><path d="M4 12a8 8 0 0 1 14-5M20 12a8 8 0 0 1-14 5"/><path d="M18 3v4h-4M6 21v-4h4"/></svg></span><h3>24/7 Support</h3><p>Round-the-clock emergency response and support.</p><span class="more">Learn More <svg width="8" height="8" viewBox="0 0 10 10"><path d="M1 5h7M5 2l3 3-3 3" stroke="currentColor" fill="none" stroke-width="1.3"/></svg></span></div>
      <div class="why-card"><span class="why-icon"><svg viewBox="0 0 24 24"><path d="M4 20L14 10M14 4l6 6-3 3-6-6zM4 4l16 16"/></svg></span><h3>Modern Equipment</h3><p>Latest traffic control technology and equipment.</p><span class="more">Learn More <svg width="8" height="8" viewBox="0 0 10 10"><path d="M1 5h7M5 2l3 3-3 3" stroke="currentColor" fill="none" stroke-width="1.3"/></svg></span></div>
    </div>
    <div class="stats">
      <div class="stat-row">
        <div class="stat"><b>500+</b><span>Projects Completed</span></div>
        <div class="stat"><b>100%</b><span>Safety Record</span></div>
        <div class="stat"><b>50+</b><span>Expert Staff</span></div>
      </div>
      <span class="btn">Contact Us</span>
    </div>
  </div>
</section>

<footer class="footer">
  <div class="wrap">
    <div class="fcols">
      <div class="fcol"><h4>Quick Links</h4><ul><li>Services</li><li>About Us</li><li>Contact</li><li>Careers</li></ul></div>
      <div class="fcol"><h4>Contact Info</h4><ul>
        <li><svg viewBox="0 0 24 24"><path d="M12 21s-6-6-6-11a6 6 0 0 1 12 0c0 5-6 11-6 11z"/><circle cx="12" cy="10" r="2"/></svg>480 Meridian Way, Houston, TX 77002</li>
        <li><svg viewBox="0 0 24 24"><path d="M5 3h4l2 5-3 2a11 11 0 0 0 6 6l2-3 5 2v4a2 2 0 0 1-2 2A17 17 0 0 1 3 5a2 2 0 0 1 2-2z"/></svg>(555) 010-2288</li>
        <li><svg viewBox="0 0 24 24"><rect x="3" y="5" width="18" height="14"/><path d="M3 6l9 7 9-7"/></svg>info@roadward-lanes.com</li>
      </ul></div>
      <div class="fcol"><h4>Follow Us</h4><div class="socials"><span></span><span></span><span></span></div></div>
    </div>
    <div class="copy">© 2025 Roadward. All rights reserved.</div>
  </div>
</footer>
</body>
</html>
```